Manufacturer of heath beverages and shooters requires label design

We require a label design for our first beverage we are launching in the US market under the brand Meadowra Sipz. Our manufacturing facility is based in California, USA.

The name of the beverage is KorvaTum, and is a health beverage to support gut health. The final design should communicate aspects such as life, energy, nature, well-being, and good health. Logo and dimensions of the label attached.

Target Market(s)

This should appeal to a broad audience across ages and genders. We are targeting individuals who are already health conscious, as well as those who are trying to improve their health.

Industry/Entity Type

Health And Wellness

Requirements
Must have
• Info that must be included
• Attached logo
• The name "KorvaTum"
• Under the name: "Natural digestive aid and overall gut health support"
• An "Organic" icon
• Caffeine-free
• 2 fl oz (59ml)
• Shake well
• Directions:
• Add contents of bottle to 6 oz warm water. Drink first thing in the morning or after a heavy meal. For best results, consume daily.
• Leave space for the nutrition facts and ingredients (will be provided to add to the winning design).
Should not have
• No images of fruit. This is not a fruit beverage.

```html
<!DOCTYPE html>
<html lang="en">
<head>
<meta charset="utf-8">
<title>KorvaTum Label – Meadowra Sipz</title>
<link href="https://fonts.googleapis.com/css2?family=Cabin:wght@400;600&family=Comfortaa:wght@400&family=Crimson+Text:wght@400;600&family=Lustria&family=Merienda:wght@400;700&display=swap" rel="stylesheet">
<style>
  :root {
    --page: #f8e7e1;
    --band: #dc8b51;
    --band-ink: #3b2519;
    --leaf: #88c541;
    --leaf-dark: #6aa532;
    --coral: #f27b55;
    --heading: #5b4a47;
    --ink: #1f1a17;
    --tag-ink: #4a2418;
    --soft-white: #ffffff;
    --muted-white: #f8d9cd;
    --badge-dark: #3f6b4a;
    --badge-light: #f4f1e6;
  }
  * { margin: 0; padding: 0; box-sizing: border-box; }
  html, body { width: 1200px; height: 985px; overflow: hidden; background: var(--page); }
  .label { position: relative; width: 1200px; height: 985px; background: var(--page); }

  .volume-band {
    position: absolute; left: 17px; top: 0; width: 1137px; height: 152px;
    background: var(--band); border-radius: 0 0 12px 12px;
  }
  .volume-band__text {
    position: absolute; left: 222px; top: 22px;
    font-family: "Comfortaa", sans-serif; font-size: 82px; color: var(--band-ink);
    letter-spacing: 1px; white-space: nowrap;
  }

  .top-panel {
    position: absolute; left: 17px; top: 152px; width: 1137px; height: 343px;
    background: var(--leaf);
  }
  .scallop { position: absolute; left: 17px; top: 487px; }

  .brand-box {
    position: absolute; left: 266px; top: 298px; width: 424px; height: 153px;
    background: rgba(255,255,255,0.6); border-radius: 8px;
    display: flex; align-items: center; justify-content: center;
  }
  .brand-box__name {
    font-family: "Cabin", sans-serif; font-weight: 600; font-size: 58px;
    color: var(--leaf-dark); line-height: 1.1; white-space: nowrap;
  }

  .section-title {
    position: absolute; font-family: "Lustria", serif; font-size: 29px; color: var(--heading);
    white-space: nowrap;
  }
  .directions-title { left: 799px; top: 166px; }
  .directions-text {
    position: absolute; left: 788px; top: 251px;
    font-family: "Cabin", sans-serif; font-size: 24px; line-height: 34.7px; color: var(--ink);
    white-space: nowrap;
  }

  .bottom-panel {
    position: absolute; left: 17px; top: 495px; width: 1135px; height: 490px;
    background: var(--coral);
  }

  .hero-art {
    position: absolute; left: 215px; top: 482px; width: 205px; height: 180px;
    border-radius: 50% 50% 40% 40%;
    background: radial-gradient(circle at 50% 45%, #f0a060 0%, #9ccf5a 55%, rgba(242,123,85,0) 72%);
  }
  .product-name {
    position: absolute; left: 200px; top: 640px; width: 580px; text-align: center;
    font-family: "Merienda", cursive; font-weight: 700; font-size: 96px;
    color: var(--soft-white); line-height: 1.1; white-space: nowrap;
  }
  .product-claim {
    position: absolute; left: 250px; top: 756px; width: 470px; text-align: center;
    font-family: "Merienda", cursive; font-size: 18.5px; line-height: 31px;
    color: var(--tag-ink); text-transform: uppercase;
  }

  .nutrition-title { left: 793px; top: 536px; font-size: 30px; }
  .ingredients-title { left: 798px; top: 725px; font-size: 30px; }

  .net-volume {
    position: absolute; left: 500px; top: 902px;
    font-family: "Crimson Text", serif; font-weight: 600; font-size: 27px; color: var(--ink);
    white-space: nowrap;
  }
  .caffeine-free {
    position: absolute; left: 473px; top: 939px;
    font-family: "Crimson Text", serif; font-size: 27px; font-variant: small-caps;
    letter-spacing: 1px; color: var(--soft-white); white-space: nowrap;
  }
  .organic-badge { position: absolute; left: 654px; top: 858px; }
  .shake-note {
    position: absolute; left: 800px; top: 946px;
    font-family: "Crimson Text", serif; font-size: 27px; color: var(--muted-white);
    text-transform: uppercase; letter-spacing: 0.5px; white-space: nowrap;
  }
</style>
</head>
<body>
<main class="label">
  <header class="volume-band">
    <p class="volume-band__text">2 fl oz /59ml</p>
  </header>

  <section class="top-panel"></section>
  <section class="bottom-panel"></section>

  <svg class="scallop" width="1137" height="18" viewBox="0 0 1137 18" aria-hidden="true">
    <defs>
      <pattern id="scallop-edge" width="33" height="18" patternUnits="userSpaceOnUse">
        <rect width="33" height="8" fill="#88c541"/>
        <circle cx="16.5" cy="6" r="11" fill="#88c541"/>
      </pattern>
    </defs>
    <rect width="1137" height="18" fill="url(#scallop-edge)"/>
  </svg>

  <div class="brand-box">
    <p class="brand-box__name">Meadowra Sipz</p>
  </div>

  <h2 class="section-title directions-title">Directions:</h2>
  <p class="directions-text">Add contents of bottle to 6 oz<br>warm water. Drink first thing<br>in the morning or after a heavy<br>meal. For best results, consume<br>daily.</p>

  <div class="hero-art" role="img" aria-label="Illustration of a leaping dancer silhouette beneath a spray of green and orange leaves"></div>
  <h1 class="product-name">KorvaTum</h1>
  <p class="product-claim">Natural digestive aid<br>and overall gut health support</p>

  <h2 class="section-title nutrition-title">Nutrition facts</h2>
  <h2 class="section-title ingredients-title">Ingredients</h2>

  <p class="net-volume">2 fl oz (59ml)</p>
  <p class="caffeine-free">Caffeine-free</p>
  <svg class="organic-badge" width="112" height="112" viewBox="0 0 112 112" role="img" aria-label="Organic certification badge">
    <circle cx="56" cy="56" r="55" fill="var(--badge-dark)"/>
    <circle cx="56" cy="56" r="41" fill="var(--badge-light)"/>
  </svg>
  <p class="shake-note">Shake well before use</p>
</main>
</body>
</html>
```